New menu design for small coffee shop

I need to design a new menu for a small cafe called The Kettle Wren. I've attached pictures of the old menu to give an idea, I really want a completely new look though. You'll notice that the food, coffee and drinks are currently on separate menus, I want all of this to be on one menu. We want to add images of the food before we print the menu, so ideally you will leave spaces for images of the food.
I'm open to suggestions on paper size and how its folded etc.
I've also attached a word file which has changes for the new menu; some are pricing updates, some are completely different.
Our Facebook page is https://www.socialpage.example/thekettlewren/ might give you an idea of what we're about.
Any other questions let me know.

```html
<!DOCTYPE html>
<html lang="en">
<head>
<meta charset="utf-8">
<title>The Kettle Wren – Menu</title>
<link href="https://fonts.googleapis.com/css2?family=Kaushan+Script&family=Lato:wght@400;700;900&display=swap" rel="stylesheet">
<style>
:root{
  --bg:#d9d9db;
  --paper:#ffffff;
  --paper-shade:#f1f1f1;
  --yellow:#ffe500;
  --wood:#5b3720;
  --wood-dark:#3f2414;
  --rust:#b4521d;
  --ink:#5a2b12;
  --ink-soft:#6e4a36;
  --night:#1c1715;
}
*{box-sizing:border-box;margin:0;padding:0}
html,body{width:1200px;height:1200px;overflow:hidden;background:var(--bg);font-family:"Lato",sans-serif;color:var(--ink)}
.sheet{position:absolute;left:20px;width:1160px;height:565px;display:grid;grid-template-columns:repeat(3,1fr);box-shadow:0 6px 18px rgba(0,0,0,.18);background:var(--paper)}
.sheet--outside{top:20px}
.sheet--inside{top:610px}
.panel{position:relative;display:flex;flex-direction:column;overflow:hidden;border-right:1px solid #e3e3e3}
.panel:last-child{border-right:none}
.wood{background:linear-gradient(180deg,var(--wood),var(--wood-dark));}
.script{font-family:"Kaushan Script",cursive;color:var(--ink)}
.photo{background:linear-gradient(135deg,#8a5a3a,#c9925e 55%,#e9c98f)}
.photo--dark{background:radial-gradient(circle at 50% 40%,#4a3a30,var(--night) 70%)}
.photo--greens{background:linear-gradient(135deg,#6e4028,#c4703a 40%,#79a04a 75%,#e9e2d2)}
.photo--table{background:linear-gradient(135deg,#5c5560,#a79f9a 50%,#e8dfd2)}
.photo--plate{background:linear-gradient(135deg,#f3eee6,#c99a5a 45%,#9bc04c 80%)}

/* brand mark */
.brand{display:flex;align-items:center;gap:8px}
.brand__dot{width:34px;height:34px;border-radius:50%;background:var(--yellow);flex:none}
.brand__name{font-family:"Lato",sans-serif;font-weight:900;font-size:16px;color:var(--ink);letter-spacing:.5px;white-space:nowrap}
.brand--light .brand__name{color:#fff}

/* menu lists */
.menu-list{list-style:none;padding:0 22px;font-size:10.5px;line-height:1.3;color:var(--ink)}
.menu-list li{display:flex;gap:8px;padding:6px 0;border-bottom:1px solid #e4dcd6}
.menu-list li::before{content:"";width:5px;height:5px;border-radius:50%;background:var(--rust);margin-top:5px;flex:none}
.menu-list .item{flex:1}
.menu-list .price{font-weight:700;white-space:nowrap}

/* breakfast */
.breakfast__head{height:60px;background:linear-gradient(180deg,var(--wood) 0 14px,var(--yellow) 14px);display:flex;flex-direction:column;align-items:center;justify-content:center;padding-top:12px}
.breakfast__title{font-size:20px}
.ribbon{background:var(--rust);color:#fff;font-weight:900;font-size:12px;letter-spacing:1px;padding:2px 26px;margin-top:2px}
.breakfast .menu-list{flex:1;padding-top:10px}
.feature{height:20px}
.feature-box{background:var(--yellow);padding:16px 24px;font-size:13px;line-height:1.45;color:var(--ink);height:120px}
.feature-box strong{font-size:15px}

/* rise panel */
.rise__photo{height:230px;display:flex;align-items:center;justify-content:center}
.rise__body{flex:1;text-align:center;padding:16px 20px 0;background:linear-gradient(180deg,var(--paper),var(--paper-shade))}
.rise__title{font-size:28px}
.rise__addr{font-size:10px;color:var(--rust);margin-top:6px}
.rise__call{font-size:13px;font-weight:700;color:var(--rust);margin-top:2px}
.rise__tag{font-family:"Kaushan Script",cursive;font-size:13px;margin-top:10px;border-top:1px solid #d8cfc8;padding-top:6px}
.thumbs{display:grid;grid-template-columns:repeat(3,1fr);gap:4px;background:var(--yellow);padding:4px;margin-top:8px}
.thumbs div{height:62px}
.web{height:52px;display:flex;align-items:center;justify-content:center;color:#fff;font-size:12px;letter-spacing:3px}

/* milkshake */
.shake__top{height:240px;background:var(--yellow);display:flex;align-items:center;justify-content:center}
.shake__circle{width:170px;height:170px;border-radius:50%;border:5px solid #fff}
.shake__body{flex:1;display:flex;flex-direction:column;align-items:center;padding-top:14px;background:linear-gradient(180deg,var(--paper),var(--paper-shade))}
.shake__lead{font-size:22px;margin-top:14px;text-align:center;line-height:1.2}
.shake__lead b{display:block;font-size:26px;font-weight:400}
.shake__sub{font-size:13px;color:var(--ink-soft);margin-top:4px}
.web--tall{height:92px}

/* lunch */
.lunch__photo{height:175px}
.lunch__title{text-align:center;font-size:20px;margin-top:10px}
.lunch__sub{text-align:center;font-size:16px;font-weight:700;color:var(--ink)}
.lunch .menu-list{flex:1;padding-top:6px}
.call-box{background:var(--yellow);height:120px;display:flex;flex-direction:column;justify-content:center;padding-left:40px;font-weight:900;color:var(--ink)}
.call-box__label{display:flex;align-items:center;gap:8px;font-size:24px}
.call-box__num{font-size:26px}

/* middle inside */
.open__photo{height:175px}
.open__ribbon{align-self:center;background:var(--rust);color:#fff;font-size:12px;font-weight:700;padding:4px 20px;margin-top:-12px;position:relative}
.open .menu-list{padding-top:4px}
.frames{display:grid;grid-template-columns:1fr 1fr;gap:6px;background:var(--yellow);padding:5px;margin:6px 20px}
.frames div{height:72px;border:2px solid #fff}
.extra{font-size:10.5px;padding:2px 22px;color:var(--ink)}
.sizes{display:flex;gap:14px;justify-content:flex-end;font-size:10.5px;padding:0 22px;font-weight:700}

/* thanks */
.thanks__art{height:200px;margin:20px 40px 0;background:linear-gradient(135deg,#f6efe9,#ead9cc);border-radius:6px}
.thanks__band{height:70px;margin-top:20px;background:linear-gradient(180deg,var(--yellow) 0 12px,var(--wood) 12px 58px,var(--yellow) 58px);display:flex;align-items:center;justify-content:center}
.thanks__band .brand{background:#fff;padding:6px 14px;border-radius:30px}
.thanks__photo{flex:1}
</style>
</head>
<body>

<section class="sheet sheet--outside">
  <article class="panel breakfast">
    <header class="breakfast__head">
      <h2 class="script breakfast__title">All Day Breakfast Menu</h2>
      <span class="ribbon">MENU</span>
    </header>
    <ul class="menu-list">
      <li><span class="item">Eggs on Turkish toast</span><span class="price">$8.0</span></li>
      <li><span class="item">Bacon and Eggs on Turkish Toast with grilled Tomato</span><span class="price">$15.0</span></li>
      <li><span class="item">Eggs Benedict - poached eggs with bacon, ham or smoked salmon and wilted baby spinach and finished with Hollandaise Sauce</span><span class="price">$18.0</span></li>
      <li><span class="item">Veggie Brekki - Our own special smashed avocado on grilled Portobello mushroom, with poached eggs, danish feta and baby Spinach.</span><span class="price">$16.0</span></li>
      <li><span class="item">High protein overnight oats - Our own protein enriched Greek yoghurt, oats and honey, topped with sliced banana</span><span class="price">$15.0</span></li>
      <li><span class="item">Omelette of the day - served with toasted Turkish bread and grilled tomato</span><span class="price">$18.0</span></li>
      <li><span class="item">Waffles - freshly toasted Waffles, maple syrup, strawberries and banana with ice cream or Cream</span><span class="price">$15.0</span></li>
      <li><span class="item">Fruit Toast</span><span class="price">$6.0</span></li>
      <li><span class="item">multigrain or White Toast with butter</span><span class="price">$4.0</span></li>
    </ul>
    <div class="wood feature"></div>
    <p class="feature-box">Wren breakfast - grilled smokey bacon, eggs, thick pork sausage, grilled mushroom topped with a lightly spiced tomato chutney, grilled tomato, lamb cutlet and hash brown with Turkish bread. <strong>$21.0</strong></p>
  </article>

  <article class="panel rise">
    <div class="rise__photo photo--dark" role="img" aria-label="Dark close-up photo of a plated breakfast">
      <div class="brand brand--light"><span class="brand__dot"></span><span class="brand__name">The Kettle Wren</span></div>
    </div>
    <div class="rise__body">
      <h2 class="script rise__title">Rise and shine!</h2>
      <p class="rise__addr">12/8 Orchard Lane 4100 Maple Grove</p>
      <p class="rise__call">call us now: +61 7 5550 1427</p>
      <p class="rise__tag">Enjoy with our delicious coffee and dishes</p>
      <div class="thumbs">
        <div class="photo" role="img" aria-label="Photo of a latte with latte art"></div>
        <div class="photo--greens" role="img" aria-label="Photo of a cooked breakfast plate"></div>
        <div class="photo--plate" role="img" aria-label="Photo of a loaded dessert"></div>
      </div>
    </div>
    <div class="wood web">www.kettlewren.example</div>
  </article>

  <article class="panel shake">
    <div class="shake__top">
      <div class="shake__circle photo--table" role="img" aria-label="Round photo of a loaded milkshake"></div>
    </div>
    <div class="shake__body">
      <div class="brand"><span class="brand__dot"></span><span class="brand__name">The Kettle Wren</span></div>
      <p class="script shake__lead">Come down &amp;<b>Treat yourself to</b></p>
      <p class="shake__sub">our new loaded milkshake</p>
    </div>
    <div class="wood web web--tall">www.kettlewren.example</div>
  </article>
</section>

<section class="sheet sheet--inside">
  <article class="panel lunch">
    <div class="lunch__photo photo--greens" role="img" aria-label="Photo of Thai beef salad"></div>
    <h2 class="script lunch__title">Lunch Menu</h2>
    <p class="lunch__sub">(from 11:30)</p>
    <ul class="menu-list">
      <li><span class="item">BLT - roast garlic Aioli, tomato chutney, smoked Bacon, Mixed Lettuce and tomato on toasted Turkish bread with fries</span><span class="price">$12.0</span></li>
      <li><span class="item">Chicken Caesar Burger or Wrap - Marinated Chicken, smoked bacon, Parmesan cheese, and coz lettuce in a toasted Turkish bread or wrap, with fries</span><span class="price">$15.0</span></li>
      <li><span class="item">Wren beef burger - juicy beef patty, smoked bacon, mixed lettuce, tomato, beetroot, caramelised onion with relish and aioli, on grilled Turkish bread with Fries</span><span class="price">$17.0</span></li>
    </ul>
    <div class="wood feature"></div>
    <div class="call-box">
      <span class="call-box__label">
        <svg width="24" height="24" viewBox="0 0 24 24" aria-hidden="true"><circle cx="12" cy="12" r="10.5" fill="none" stroke="currentColor" stroke-width="2"/><path d="M8 6.5c-.8 0-1.5.8-1.3 1.8.6 3.8 4.1 7.6 8 8.6 1 .2 1.8-.4 1.9-1.2l.2-1.2-2.6-1.2-1 1c-1.4-.6-2.8-2-3.4-3.4l1-1-1.2-2.6z" fill="currentColor"/></svg>
        Call us now:
      </span>
      <span class="call-box__num">+61 7 5550 1427</span>
    </div>
  </article>

  <article class="panel open">
    <div class="open__photo photo--table" role="img" aria-label="Overhead photo of loaded milkshakes on a table"></div>
    <span class="open__ribbon">We are open 7am - 2pm</span>
    <ul class="menu-list">
      <li><span class="item">Caesar salad - crispy coz lettuce, smoky bacon, Parmesan Cheese, herbed croutons all tossed together with Caesar dressing and finished with a poached egg</span><span class="price">$14.0</span></li>
    </ul>
    <p class="extra">Add chicken, Salmon or Avocado <b style="float:right">$3</b></p>
    <div class="frames">
      <div class="photo" role="img" aria-label="Photo of a toasted roll"></div>
      <div class="photo--plate" role="img" aria-label="Photo of a cake"></div>
    </div>
    <ul class="menu-list">
      <li><span class="item">Thai beef salad - Marinated slices of tender Eye fillet steak, Mixed lettuce, Julienne vegetables, fresh coriander and mint with our special Thai dressing</span><span class="price">$17.0</span></li>
      <li><span class="item">Quinoa salad - Roast root vegetables with pomegranate, walnuts, baby Spinach and balsamic dressing.</span><span class="price">$15.0</span></li>
      <li><span class="item">Chips</span></li>
    </ul>
    <div class="sizes"><span>Small $4</span><span>Large $7</span></div>
    <div class="wood" style="flex:1;margin-top:6px"></div>
  </article>

  <article class="panel thanks">
    <div class="thanks__art" role="img" aria-label="Hand-lettered Thank you in brown script"></div>
    <div class="thanks__band">
      <div class="brand"><span class="brand__dot"></span><span class="brand__name">The Kettle Wren</span></div>
    </div>
    <div class="thanks__photo photo--plate" role="img" aria-label="Photo of a breakfast plate with avocado, mushrooms and halloumi"></div>
  </article>
</section>

</body>
</html>
```